new roofing company card

New primary business card for roofing company.

Industry/Entity Type

Residential roofing/Specializing in Asphalt and Standing seam metal roofing

Contact Information for Business Card

Phone number is: 484 672 1058 Email: support@fennridgeroofworks.com website: www.fennridgeroofworks.com

Colors
EB3D1F
EC4F4E
F09395
F8D3D4
FCEDEE

```html
<!DOCTYPE html>
<html lang="en">
<head>
<meta charset="utf-8">
<title>Fennridge Roofworks – Business Card</title>
<link rel="stylesheet" href="https://fonts.googleapis.com/css2?family=Cinzel:wght@400;600&family=Roboto:wght@400&display=swap">
<style>
  :root {
    --stage: #2a2a2a;
    --card-white: #ffffff;
    --ink: #232323;
    --brand-red: #c8302a;
    --brand-red-light: #d63a2f;
    --rule: #9a9a9a;
    --text-grey: #2b2b2b;
  }
  * { box-sizing: border-box; margin: 0; padding: 0; }
  html, body { width: 1200px; height: 1108px; overflow: hidden; }
  body {
    background: var(--stage);
    position: relative;
    font-family: "Roboto", Arial, sans-serif;
  }
  .card {
    position: absolute;
    top: 186px;
    width: 420px;
    height: 735px;
    border-radius: 22px;
    overflow: hidden;
  }
  .card-front { left: 150px; background: var(--card-white); }
  .card-back { left: 630px; background: var(--brand-red); }

  .brand-block {
    position: absolute;
    top: 150px;
    left: 0;
    width: 100%;
    text-align: center;
  }
  .brand-name {
    font-family: "Cinzel", Georgia, serif;
    font-weight: 600;
    color: var(--ink);
    font-size: 46px;
    line-height: 1.05;
    letter-spacing: 1px;
  }
  .brand-mark {
    display: block;
    width: 22px;
    height: 22px;
    margin: 0 auto 22px;
    background: var(--brand-red);
  }

  .person {
    position: absolute;
    top: 430px;
    width: 100%;
    text-align: center;
  }
  .person-name {
    font-family: "Cinzel", Georgia, serif;
    font-weight: 400;
    font-size: 27px;
    color: var(--ink);
    letter-spacing: 1px;
  }
  .person-role {
    font-size: 20px;
    color: var(--brand-red);
    margin-top: 2px;
  }

  .contact-icons {
    position: absolute;
    top: 512px;
    left: 50px;
    right: 50px;
    display: flex;
    align-items: center;
    gap: 10px;
  }
  .contact-icons .rule { flex: 1; height: 1px; background: var(--rule); }
  .icon-tile {
    width: 34px;
    height: 34px;
    border-radius: 5px;
    background: var(--brand-red);
    display: flex;
    align-items: center;
    justify-content: center;
  }
  .icon-tile svg { width: 22px; height: 22px; }

  .contact-list {
    position: absolute;
    top: 566px;
    width: 100%;
    text-align: center;
    list-style: none;
    font-size: 18px;
    line-height: 1.5;
    color: var(--text-grey);
  }
  .contact-list .phone { font-size: 21px; }
  .contact-list .domain { color: var(--brand-red); }

  .back-pattern {
    position: absolute;
    inset: 0;
    background: linear-gradient(160deg, var(--brand-red-light) 0%, var(--brand-red) 55%, #b82a25 100%);
  }
</style>
</head>
<body>
  <section class="card card-front">
    <div class="brand-block">
      <span class="brand-mark"></span>
      <div class="brand-name">FENNRIDGE<br>ROOFWORKS</div>
    </div>

    <div class="person">
      <div class="person-name">DANIEL HARPER</div>
      <div class="person-role">Managing Director</div>
    </div>

    <div class="contact-icons">
      <span class="rule"></span>
      <span class="icon-tile" aria-label="Phone">
        <svg viewBox="0 0 24 24"><path fill="#fff" d="M6.6 10.8a15 15 0 0 0 6.6 6.6l2.2-2.2a1 1 0 0 1 1-.25 11.4 11.4 0 0 0 3.6.57 1 1 0 0 1 1 1V20a1 1 0 0 1-1 1A17 17 0 0 1 3 4a1 1 0 0 1 1-1h3.5a1 1 0 0 1 1 1c0 1.25.2 2.45.57 3.57a1 1 0 0 1-.25 1z"/></svg>
      </span>
      <span class="icon-tile" aria-label="Email">
        <svg viewBox="0 0 24 24"><rect x="3" y="6" width="18" height="12" rx="1" fill="none" stroke="#fff" stroke-width="1.8"/><path d="M3.5 6.5 12 13l8.5-6.5" fill="none" stroke="#fff" stroke-width="1.8"/></svg>
      </span>
      <span class="icon-tile" aria-label="Website">
        <svg viewBox="0 0 24 24"><circle cx="12" cy="12" r="8.5" fill="none" stroke="#fff" stroke-width="1.8"/><path d="M3.5 12h17M12 3.5c3 3 3 14 0 17M12 3.5c-3 3-3 14 0 17" fill="none" stroke="#fff" stroke-width="1.4"/></svg>
      </span>
      <span class="rule"></span>
    </div>

    <ul class="contact-list">
      <li class="phone">484 672 1058</li>
      <li>support@fennridgeroofworks.com</li>
      <li>www.<span class="domain">fennridgeroofworks</span>.com</li>
    </ul>
  </section>

  <section class="card card-back">
    <div class="back-pattern" role="img" aria-label="Repeating glossy brand monogram pattern on red"></div>
  </section>
</body>
</html>
```